Maple Glow Label

Design a label for new brand called Maple Glow. The specific product label :
Maple Glow Cocoa Butter Lotion. You only need to design the front label.
I have included the logo and a bottle jpeg with 2 bottles on it. Please try your best.

Requirements
Must have
• text on the label other than the logo:
cocoa butter
lotion
8.5oz/250ml

Original Moisturizing Formula
Smoothes Marks
Protect Skin

__________________________________
- ALTERNATIVE TEXT TO ALSO USE:
Smoothes Dry Skin, Blemishes & Stretch Marks
Softens Hands, Face and Body
Vitamin E

```html
<!DOCTYPE html>
<html lang="en">
<head>
<meta charset="utf-8">
<title>Maple Glow Cocoa Butter Lotion – Front Labels</title>
<link href="https://fonts.googleapis.com/css2?family=Roboto:wght@400;700&display=swap" rel="stylesheet">
<style>
  :root {
    --canvas: #f4f2ef;
    --label-white: #ffffff;
    --cream: #f4d3a2;
    --peach: #f7c79b;
    --rose: #b8386a;
    --pink: #ec1a6d;
    --gold: #b98b3e;
    --gold-deep: #9a7431;
    --gold-light: #f5e887;
    --ink: #5b4a3a;
  }
  html, body {
    margin: 0;
    padding: 0;
    width: 1200px;
    height: 849px;
    overflow: hidden;
    background: var(--canvas);
    font-family: "Roboto", Arial, sans-serif;
  }
  .canvas {
    position: relative;
    width: 1200px;
    height: 849px;
  }
  .label {
    position: absolute;
    top: 190px;
    height: 470px;
    box-shadow: 0 2px 10px rgba(0,0,0,0.08);
  }
  .label--pump { left: 300px; width: 250px; }
  .label--flip { left: 640px; width: 270px; }
  .label svg { display: block; width: 100%; height: 100%; }
  .brand-name { font-family: "Roboto", Arial, sans-serif; font-weight: 700; font-size: 30px; fill: var(--pink); }
  .product-name { font-weight: 400; fill: var(--gold); letter-spacing: 2px; }
  .product-name--on-gold { fill: var(--gold-deep); }
  .claims { font-weight: 700; font-size: 8.5px; letter-spacing: 0.6px; }
  .claims--light { fill: var(--label-white); }
  .claims--gold { fill: var(--gold); }
  .volume { font-size: 8px; letter-spacing: 0.8px; fill: var(--ink); }
</style>
</head>
<body>
<main class="canvas">

  <section class="label label--pump" aria-label="Maple Glow cocoa butter lotion label, pump bottle">
    <svg viewBox="0 0 250 470" xmlns="http://www.w3.org/2000/svg">
      <defs>
        <linearGradient id="pump-top" x1="0" y1="1" x2="1" y2="0">
          <stop offset="0" stop-color="#fbe3c4"/>
          <stop offset="0.55" stop-color="var(--peach)"/>
          <stop offset="1" stop-color="var(--rose)"/>
        </linearGradient>
        <linearGradient id="pump-wave" x1="0" y1="0" x2="1" y2="1">
          <stop offset="0" stop-color="#fdf1e3"/>
          <stop offset="1" stop-color="#f6d8b6"/>
        </linearGradient>
      </defs>
      <rect class="label-base" width="250" height="470" fill="var(--cream)"/>
      <path class="label-top-band" d="M0 0 H250 V70 C180 60 90 110 0 95 Z" fill="url(#pump-top)"/>
      <path class="label-cream-wave" d="M0 95 C90 110 180 60 250 70 V200 C170 215 100 270 0 300 Z" fill="url(#pump-wave)"/>
      <path class="label-pink-field" d="M0 300 C100 270 170 215 250 200 V420 C170 405 80 400 0 430 Z" fill="var(--pink)"/>
      <path class="label-pink-shade" d="M0 300 C60 282 100 262 140 245 C110 275 60 300 0 320 Z" fill="#f59a7a" opacity="0.7"/>

      <text class="brand-name" x="125" y="118" text-anchor="middle">Maple Glow</text>
      <text class="product-name" x="60" y="178" font-size="17">cocoa butter</text>
      <text class="product-name" x="60" y="196" font-size="12">lotion</text>

      <text class="claims claims--light" x="20" y="338">Original Moisturizing Formula</text>
      <text class="claims claims--light" x="20" y="350">Smoothes Marks</text>
      <text class="claims claims--light" x="20" y="362">Protect Skin</text>

      <text class="volume" x="20" y="452">8.5oz/250ml</text>
    </svg>
  </section>

  <section class="label label--flip" aria-label="Maple Glow cocoa butter lotion label, flip-cap bottle">
    <svg viewBox="0 0 270 470" xmlns="http://www.w3.org/2000/svg">
      <defs>
        <linearGradient id="flip-gold" x1="0" y1="1" x2="1" y2="0">
          <stop offset="0" stop-color="var(--gold)"/>
          <stop offset="0.5" stop-color="#dcbc68"/>
          <stop offset="1" stop-color="var(--gold-light)"/>
        </linearGradient>
      </defs>
      <rect class="label-base" width="270" height="470" fill="var(--label-white)"/>
      <path class="label-top-arc" d="M40 70 C100 20 190 20 245 55 C190 35 110 40 40 70 Z" fill="var(--pink)"/>
      <path class="label-side-curve" d="M264 160 C252 272 162 332 40 346 C165 338 250 288 264 198 Z" fill="var(--pink)"/>
      <path class="label-gold-field" d="M264 200 C250 292 165 340 44 350 C38 362 36 374 38 384 C120 390 192 412 226 456 C236 420 250 392 264 362 Z" fill="url(#flip-gold)"/>

      <text class="brand-name" x="135" y="135" text-anchor="middle">Maple Glow</text>

      <text class="claims claims--gold" x="22" y="230">Original Moisturizing Formula</text>
      <text class="claims claims--gold" x="22" y="242">Smoothes Marks</text>
      <text class="claims claims--gold" x="22" y="254">Protect Skin</text>

      <text class="product-name product-name--on-gold" x="50" y="372" font-size="19">cocoa butter</text>
      <text class="product-name product-name--on-gold" x="178" y="391" font-size="13">lotion</text>

      <text class="volume" x="22" y="455">8.5oz/250ml</text>
    </svg>
  </section>

</main>
</body>
</html>
```